BUSINESS CARD DESIGN

NAME- TODD MASVERIK
PHONE NUMER - 808- 451-7082
EMAIL- OFFICE@VORLINDE-GRADEWAY.COM
BACK OF CARD- SPEACIALIZES IN LAND CLEARING, FORESTRY MUCLHING AND EXCAVATION

Contact Information for Business Card

NAME- TODD MASVERIK PHONE NUMER - 808- 451-7082 EMAIL- OFFICE@VORLINDE-GRADEWAY.COM BACK OF CARD- SPEACIALIZES IN LAND CLEARING , MUCLHING AND EXCAVATION

```html
<!DOCTYPE html>
<html lang="en">
<head>
<meta charset="UTF-8">
<title>Vorlinde Gradeway – Business Card</title>
<link href="https://fonts.googleapis.com/css2?family=Montserrat:wght@300;400;500;600;700&display=swap" rel="stylesheet">
<style>
  :root {
    --backdrop: #4a4a4a;
    --card: #000000;
    --accent: #ffc107;
    --text-light: #ffffff;
  }
  * { margin: 0; padding: 0; box-sizing: border-box; }
  html, body {
    width: 1120px; height: 1200px; overflow: hidden;
    background: var(--backdrop);
    font-family: 'Montserrat', sans-serif;
  }
  .card {
    position: absolute; left: 110px;
    width: 900px; height: 514px;
    background: var(--card);
    border-radius: 22px;
    overflow: hidden;
    box-shadow: 0 14px 30px rgba(0,0,0,0.45);
  }
  .card--front { top: 50px; }
  .card--back { top: 636px; }
  .band {
    position: absolute; left: 0; right: 0; bottom: 0;
    height: 34px; background: var(--accent);
  }
  .tab { position: absolute; background: var(--accent); }
  .tab--top { top: 0; right: 200px; width: 60px; height: 26px; }
  .tab--side { left: 0; top: 150px; width: 56px; height: 26px; }

  .brand {
    position: absolute; display: flex; flex-direction: column; align-items: center;
    color: var(--accent);
  }
  .card--front .brand { left: 0; right: 0; top: 150px; }
  .card--back .brand { left: 190px; top: 60px; width: 320px; }
  .brand__mark {
    width: 86px; height: 86px; border-radius: 50%;
    background: var(--accent); margin-bottom: 18px;
  }
  .brand__name {
    font-weight: 700; font-size: 34px; letter-spacing: 2px; line-height: 1.1;
    text-align: center;
  }
  .brand__sub {
    font-weight: 700; font-size: 17px; letter-spacing: 10px; margin-top: 6px;
  }
  .brand__phone {
    font-weight: 700; font-size: 17px; letter-spacing: 12px; margin-top: 10px;
  }

  .holder {
    position: absolute; left: 280px; top: 300px; width: 560px;
  }
  .holder__name {
    font-size: 34px; color: var(--text-light); font-weight: 300; letter-spacing: 1px;
    text-align: center;
  }
  .holder__name strong { color: var(--accent); font-weight: 700; }
  .holder__rule { height: 2px; background: var(--accent); margin: 12px 0 10px; }
  .holder__specialty {
    color: var(--accent); font-weight: 600; font-size: 17px; letter-spacing: 0.5px;
    text-align: center;
  }
  .contacts {
    position: absolute; left: 330px; top: 420px;
    display: flex; gap: 60px;
    color: var(--text-light); font-size: 17px; font-weight: 500;
  }
  .contact { display: flex; align-items: center; gap: 14px; }
  .contact svg { width: 22px; height: 22px; }
</style>
</head>
<body>
  <section class="card card--front">
    <div class="brand">
      <div class="brand__mark"></div>
      <div class="brand__name">VORLINDE GRADEWAY</div>
      <div class="brand__sub">LLC</div>
      <div class="brand__phone">808 451 7082</div>
    </div>
    <div class="band"></div>
  </section>

  <section class="card card--back">
    <div class="tab tab--top"></div>
    <div class="tab tab--side"></div>
    <div class="brand">
      <div class="brand__mark"></div>
      <div class="brand__name">VORLINDE GRADEWAY</div>
      <div class="brand__sub">LLC</div>
      <div class="brand__phone">808 451 7082</div>
    </div>
    <div class="holder">
      <div class="holder__name"><strong>TODD</strong> MASVERIK</div>
      <div class="holder__rule"></div>
      <div class="holder__specialty">SPEACIALIZES IN LAND CLEARING , MUCLHING AND EXCAVATION</div>
    </div>
    <div class="contacts">
      <div class="contact">
        <svg viewBox="0 0 24 24" fill="none" stroke="#ffffff" stroke-width="1.6">
          <path d="M5 3h4l2 5-3 2a12 12 0 0 0 6 6l2-3 5 2v4a2 2 0 0 1-2 2A18 18 0 0 1 3 5a2 2 0 0 1 2-2z"/>
        </svg>
        <span>808- 451-7082</span>
      </div>
      <div class="contact">
        <svg viewBox="0 0 24 24" fill="none" stroke="#ffffff" stroke-width="1.6">
          <rect x="2" y="5" width="20" height="14" rx="1"/>
          <path d="M2 6l10 7 10-7"/>
        </svg>
        <span>OFFICE@VORLINDE-GRADEWAY.COM</span>
      </div>
    </div>
    <div class="band"></div>
  </section>
</body>
</html>
```